Quick Straightforward Billboard Redesign

- Design billboard sized for 10 foot' x 36' foot width live area size and please include bleeds 6" around all sides
- Exact blue color match is imperative in headline, logo, phone number bubble or wherever used. C-83 / M-45 / Y-1 / K-0-
- What I hope to illustrate is that our company offers the best porch screening in the area area, in regards to quality, expertise, durability, storms proof, but we do not build screen porches.
- Current board is attached below from previous designer, and as you can see sizing was off, white space on edges make it appear to be sized incorrectly.
- I also attached my own little mock up idea well well if it helps, favorite image, logo, headline, etc and ideas perhaps on expanding or making this better?

Thanks so much!

Target Market(s)

Drivers and passengers, Southeastern NC, are of immense new construction and high end homes.

Industry/Entity Type

Construction

Colors
0054AA
0677BA
7BADD7
CADEEF
E8F1F8

Requirements
Must have
• Blue color matching
Nice to have
• Design spins or other thoughts on my little mock up

```html
<!DOCTYPE html>
<html lang="en">
<head>
<meta charset="utf-8">
<title>Tidewater Screens Billboard</title>
<link href="https://fonts.googleapis.com/css2?family=Anton&family=Oswald:wght@600&display=swap" rel="stylesheet">
<style>
  :root {
    --brand-blue: #0667B3;
    --coast-green: #1BB15A;
    --white: #ffffff;
    --backdrop: #383838;
    --sky: #8FC3E8;
    --lawn: #7FA35A;
    --wicker: #6E675E;
    --ceiling: #EEF1F2;
  }
  * { margin: 0; padding: 0; box-sizing: border-box; }
  html, body { width: 1200px; height: 480px; overflow: hidden; background: var(--backdrop); }
  .billboard {
    position: absolute; left: 0; top: 61px;
    width: 1200px; height: 357px;
    background: var(--white); overflow: hidden;
  }
  .porch-photo {
    position: absolute; right: 0; top: 0;
    width: 560px; height: 357px;
    background:
      linear-gradient(180deg, var(--ceiling) 0%, var(--ceiling) 18%, var(--sky) 22%, #B9D9EE 42%, #4F7F52 52%, var(--lawn) 62%, #A8A39A 72%, var(--wicker) 100%);
    -webkit-mask-image: linear-gradient(90deg, transparent 0%, #000 38%);
            mask-image: linear-gradient(90deg, transparent 0%, #000 38%);
  }
  .headline {
    position: absolute; left: 54px; top: 38px;
    font-family: "Anton", "Impact", sans-serif;
    font-size: 86px; line-height: 86px; letter-spacing: 0.5px;
  }
  .headline .line-1 { color: var(--brand-blue); display: block; }
  .headline .line-2 { color: var(--coast-green); display: block; }
  .phone-bubble {
    position: absolute; left: 0; top: 223px;
    width: 430px; height: 83px;
    background: var(--brand-blue);
    border-radius: 0 14px 14px 0;
    box-shadow: 0 10px 14px -8px rgba(0,0,0,0.35);
    display: flex; align-items: center;
  }
  .phone-icon { position: absolute; left: 53px; top: 20px; width: 44px; height: 44px; }
  .phone-number {
    position: absolute; left: 107px; top: 6px;
    font-family: "Anton", "Impact", sans-serif;
    font-size: 58px; line-height: 70px; color: var(--white); letter-spacing: 0.5px;
  }
  .brand-name {
    position: absolute; left: 455px; top: 226px;
    display: flex; align-items: center; gap: 16px;
  }
  .brand-mark { width: 40px; height: 40px; background: var(--brand-blue); }
  .brand-text {
    font-family: "Oswald", sans-serif; font-weight: 600;
    color: var(--brand-blue); font-size: 44px; line-height: 48px;
  }
</style>
</head>
<body>
  <div class="billboard">
    <div class="porch-photo" role="img" aria-label="Photo of a covered screened porch with wicker seating and a ceiling fan, overlooking a fenced lawn and a lake"></div>

    <h1 class="headline">
      <span class="line-1">Screen Your Porch.</span>
      <span class="line-2">Built for the Coast.</span>
    </h1>

    <div class="phone-bubble">
      <svg class="phone-icon" viewBox="0 0 44 44" aria-hidden="true">
        <circle cx="22" cy="22" r="21" fill="#1BB15A" stroke="#fff" stroke-width="2"/>
        <path d="M15 13c1-1 2.5-1 3 0l2 4c.4 1-.2 1.8-1 2.5-.6.5-.6 1.2-.2 1.9 1 1.7 2.2 2.9 3.9 3.9.7.4 1.4.4 1.9-.2.7-.8 1.5-1.4 2.5-1l4 2c1 .5 1 2 0 3l-1.6 1.6c-1.5 1.5-4 1.6-6.6.2-3.5-1.9-6.8-5.2-8.7-8.7-1.4-2.6-1.3-5.1.2-6.6z" fill="#fff"/>
        <path d="M25 12a8 8 0 0 1 7 7M25 16a4 4 0 0 1 3 3" stroke="#fff" stroke-width="1.8" fill="none" stroke-linecap="round"/>
      </svg>
      <span class="phone-number">910.555.0142</span>
    </div>

    <div class="brand-name">
      <span class="brand-mark"></span>
      <span class="brand-text">TIDEWATER<br>SCREENS</span>
    </div>
  </div>
</body>
</html>
```